来年3月31日に期限が迫っているインボイス制度について、まだまだ関係ある方にも周知はされていません。
もちろん税務関係なので、税理士さんを始めとして、いろいろな方が、セミナー開催やポルネットとかでも語っていらっしゃいます。
ところが、職種によっては、今更、込み入った話など聞きたくない、面倒だ、聞いてもよく理解できないといった方が多々おられます。
私は、建築関係の経理に携わっており、身近にも、そんな方々を目にしていて危惧している状態です。
これが全国となったら、いったいどれだけの人が、わからないまま期日を迎えてしまうのでしょう。
その中で、とくに今回 ひとり親方にターゲットを絞って、せめて、その方々に向けて、いちからわかるように、しかも語りかけるつもりで書きました。
本文を添付いたしますので、その意向を汲んでいただいた上での電子書籍の表紙デザインをお願いしたいです。
一目で見て、これなら一度読んでみるかと思っていただけるようなものを期待しております。
是非とも、宜しくお願い致します。

```html
<!DOCTYPE html>
<html lang="ja">
<head>
<meta charset="utf-8">
<title>ひとり親方のための いちからわかるインボイス制度</title>
<link href="https://fonts.googleapis.com/css2?family=Noto+Sans+JP:wght@400;500;700;900&display=swap" rel="stylesheet">
<style>
  :root {
    --paper: #ffffff;
    --ink: #222222;
    --band: #f7c8a6;
    --title-blue: #1d63b0;
    --sub-green: #1f4f3c;
    --alert-red: #d62a2a;
    --art-light: #eef0f2;
    --art-mid: #d9dde2;
    --worker-a: #f1d7c3;
    --worker-b: #c9ced6;
  }
  * { margin: 0; padding: 0; box-sizing: border-box; }
  html, body { width: 750px; height: 1200px; overflow: hidden; background: var(--paper); }
  .cover {
    position: relative;
    width: 750px;
    height: 1200px;
    background: var(--paper);
    font-family: "Noto Sans JP", sans-serif;
    color: var(--ink);
    overflow: hidden;
  }
  .hero-art {
    position: absolute;
    left: 300px; top: 0;
    width: 450px; height: 480px;
    background: linear-gradient(160deg, var(--art-light) 0%, var(--art-mid) 60%, var(--paper) 100%);
  }
  .deadline {
    position: absolute;
    left: 50px; top: 28px;
    font-size: 35px;
    font-weight: 700;
    line-height: 1.3;
  }
  .lead {
    position: absolute;
    left: 30px; top: 515px;
    width: 700px;
    font-size: 28px;
    font-weight: 500;
    line-height: 1.55;
  }
  .band {
    position: absolute;
    left: 0; top: 622px;
    width: 750px; height: 578px;
    background: var(--band);
  }
  .vert {
    position: absolute;
    writing-mode: vertical-rl;
    text-orientation: mixed;
  }
  .series {
    right: 105px; top: 642px;
    font-size: 30px;
    font-weight: 700;
    line-height: 1.25;
    color: var(--sub-green);
  }
  .title {
    right: 188px; top: 690px;
    font-size: 60px;
    font-weight: 900;
    line-height: 1;
    color: var(--title-blue);
  }
  .worry {
    right: 300px; top: 645px;
    font-size: 28px;
    font-weight: 700;
    line-height: 1.35;
    letter-spacing: -1px;
    color: var(--alert-red);
  }
  .about {
    right: 420px; top: 655px;
    height: 300px;
    font-size: 20px;
    font-weight: 400;
    line-height: 1.85;
  }
  .author {
    right: 38px; top: 900px;
    font-size: 28px;
    font-weight: 500;
    letter-spacing: 6px;
  }
  .worker-art {
    position: absolute;
    left: 95px; top: 975px;
    width: 235px; height: 225px;
    background: linear-gradient(180deg, var(--worker-a) 0%, var(--worker-b) 100%);
    border-radius: 110px 110px 0 0;
  }
</style>
</head>
<body>
  <div class="cover">
    <div class="hero-art" role="img" aria-label="おもちゃのショベルカーがTAXと書かれた積み木を押している写真"></div>

    <p class="deadline">2023年3月31日<br>までの申請に<br>期限のせまった<br>インボイス制度</p>

    <p class="lead">税理士さんに任せている方も、ちゃんと理解して、<br>後悔しないために、判断するのはあなたです！</p>

    <div class="band"></div>

    <p class="vert series">ひとり親方のための<br>いちからわかる</p>
    <h1 class="vert title">インボイス制度</h1>
    <p class="vert worry">今更、込み入った話など<br>聞きたくない、面倒だ、<br>聞いてもよく理解できない・・・</p>
    <p class="vert about">建築業関連の会社をクライアントに持ち、経理、そしてそれに付随するお仕事を二十年以上させていただいてきた。現場で接している立場の著者があまりに多くの方が知らないで時を過ごしていらっしゃるのが気がかりで、わかりやすく解説しました。</p>

    <div class="worker-art" role="img" aria-label="ヘルメットをかぶり腕を組んだ作業員のイラスト"></div>

    <p class="vert author">森田春香 著</p>
  </div>
</body>
</html>
```